Skincare,Bodycare and haircare brochure

Please design a A4 3 fold brochure for Vexmira Pty Ltd. You may go to our website www.vexmira.example to understand what we do - certified organic skincare.
Content:

About Us: Our Mission
Vexmira’s mission is to make premium skin care products using only certified organic ingredients for a safer, purer world.

How are we diferent?
Vexmira specialises in the research and development of certified organic skin, hair and personal care products for everyone. We hold Certified Organic Licenses with the Verdant Tally Board who accredits our system with the Federal Harvest Purity Code of Australia and other international organic certification standards. Vexmira’s passion is to produce and deliver premium, safe and effective certified organic products to all of our customers.

Other headings: Skincare, Body Care, Hair Care, Essential Oils (leave room for us to put product pictures and product info (you can copy 3 products from each category from our website for draft),

Please provide a heading about our memberships: Please also see our website for info.

Then have a contact us section (doesn't have to be a page) It can even be on the front page.

Please also use the Attached logos. Please use vexmira logo with underline (company logo) and dunbrook crafted and Certified Organic logos.

Many deaigns dont allow me to put alotnof product infronation on it. please allow me to donsoMan

```html
<!DOCTYPE html>
<html lang="en">
<head>
<meta charset="utf-8">
<title>Vexmira Brochure</title>
<link href="https://fonts.googleapis.com/css2?family=Arimo:wght@400;700&family=Great+Vibes&family=Cinzel:wght@400&display=swap" rel="stylesheet">
<style>
  :root {
    --page-bg: #ffffff;
    --paper: #ecd9c4;
    --paper-light: #f1e4d3;
    --paper-shade: #dcc2a8;
    --brand-brown: #5b3b2d;
    --ink: #3a2a22;
    --rule: #6b4a3a;
    --photo-warm: #c98f6e;
    --photo-dark: #6a3f2c;
    --jar-green: #9fc08a;
    --jar-dark: #2f2a26;
    --gel-orange: #d0642c;
    --hair-amber: #b8834f;
  }
  * { box-sizing: border-box; margin: 0; padding: 0; }
  html, body { width: 1200px; height: 1200px; overflow: hidden; background: var(--page-bg); }
  body { position: relative; font-family: "Arimo", Arial, sans-serif; color: var(--ink); }

  .inside-spread {
    position: absolute; left: 40px; top: 290px; width: 810px; height: 620px;
    display: flex; box-shadow: 0 6px 22px rgba(0,0,0,.12);
  }
  .spread-photo {
    position: absolute; inset: 0;
    background: linear-gradient(100deg, var(--paper-light) 0%, var(--paper) 35%, #e3c6ab 60%, var(--paper) 100%);
  }
  .panel {
    position: relative; width: 270px; height: 620px; padding: 22px 22px;
    text-align: center; font-size: 10.5px; line-height: 1.32;
  }
  .panel + .panel { border-left: 1px solid rgba(107,74,58,.15); }
  .script-heading {
    font-family: "Great Vibes", cursive; font-size: 27px; font-weight: 400;
    color: var(--ink); line-height: 1.05;
  }
  .script-heading::after {
    content: ""; display: block; width: 140px; height: 1px; margin: 3px auto 7px;
    background: linear-gradient(90deg, transparent, var(--rule), transparent);
  }
  .panel p { margin-bottom: 6px; }
  .panel strong { font-weight: 700; }
  .section-gap { margin-top: 12px; }

  .oil-intro { display: flex; align-items: center; gap: 10px; text-align: left; }
  .oil-intro p { margin: 0; flex: 1; }
  .oil-bottle {
    flex: none; width: 30px; height: 52px; border-radius: 5px;
    background: linear-gradient(180deg, var(--jar-dark) 0 24%, #4a3a2e 24% 100%);
  }
  .oil-list {
    list-style: disc; text-align: left; margin: 6px 0 0 16px;
    columns: 2; column-gap: 18px; font-size: 10.5px; line-height: 1.35;
  }

  .badge-row { display: flex; justify-content: center; gap: 14px; margin-top: 6px; }
  .badge { width: 40px; height: 40px; border-radius: 50%; background: var(--brand-brown); opacity: .85; }
  .badge.square { border-radius: 4px; }

  .product-grid {
    display: grid; grid-template-columns: 1fr 1fr; gap: 22px 12px; margin-top: 22px;
  }
  .product { font-size: 10px; line-height: 1.3; }
  .product-jar {
    width: 92px; height: 82px; margin: 0 auto 7px; border-radius: 10px;
    background: linear-gradient(180deg, #8f8a84 0 20%, var(--jar-dark) 20% 30%, var(--jar-green) 30% 85%, var(--jar-dark) 85%);
  }
  .price { border-bottom: 1px solid var(--rule); padding-bottom: 1px; white-space: nowrap; }

  .pair-products { display: grid; grid-template-columns: 1fr 1fr; gap: 10px; margin-top: 8px; }
  .pump-bottle {
    width: 40px; height: 78px; margin: 0 auto 6px; border-radius: 7px 7px 5px 5px;
    background: linear-gradient(180deg, #222 0 18%, var(--gel-orange) 18%);
  }
  .pump-bottle.lotion { background: linear-gradient(180deg, #222 0 18%, var(--jar-green) 18%); }
  .pump-bottle.shampoo { background: linear-gradient(180deg, #222 0 18%, var(--hair-amber) 18%); }
  .pump-bottle.conditioner { background: linear-gradient(180deg, #222 0 18%, var(--paper-shade) 18%); }

  .cover {
    position: absolute; left: 880px; top: 290px; width: 280px; height: 620px;
    background: linear-gradient(180deg, var(--paper-light), var(--paper));
    box-shadow: 0 6px 22px rgba(0,0,0,.14); text-align: center;
  }
  .brand-block {
    margin: 0 auto; width: 214px; height: 140px; background: var(--brand-brown);
    display: flex; align-items: center; justify-content: center;
  }
  .brand-name { font-family: "Cinzel", serif; font-size: 26px; color: var(--paper-shade); letter-spacing: 2px; }
  .mission { padding: 10px 26px 0; font-size: 10px; line-height: 1.35; }
  .mission-title { font-family: "Great Vibes", cursive; font-size: 20px; line-height: 1; margin-bottom: 2px; }
  .tagline-script { font-family: "Great Vibes", cursive; font-size: 22px; margin-top: 10px; }
  .tagline { font-size: 19px; line-height: 1.05; margin-top: 2px; }
  .cover-photo {
    position: absolute; left: 0; right: 0; bottom: 44px; height: 210px;
    background: linear-gradient(160deg, var(--paper) 0%, var(--photo-warm) 45%, var(--photo-dark) 100%);
  }
  .contact {
    position: absolute; left: 0; right: 0; bottom: 0; height: 44px;
    background: var(--brand-brown); color: var(--paper-light);
    display: flex; flex-direction: column; justify-content: center; font-size: 10.5px; line-height: 1.35;
  }
  .contact-title { font-weight: 700; letter-spacing: 1px; text-transform: uppercase; font-size: 9.5px; }
</style>
</head>
<body>

<section class="inside-spread">
  <div class="spread-photo" role="img" aria-label="Faint background photo of a woman relaxing during a spa treatment"></div>

  <article class="panel panel-about">
    <h2 class="script-heading">How are we different?</h2>
    <p><strong>Vexmira</strong> specialises in the research and development of certified organic skin, hair and personal care products for everyone.</p>
    <p>We hold Certified Organic Licenses with the Verdant Tally Board who accredits our system with the Federal Harvest Purity Code of Australia and other international organic certification standards.</p>
    <p><strong>Vexmira’s</strong> passion is to produce and deliver premium, safe and effective certified organic products to all of our customers.</p>

    <div class="section-gap">
      <h2 class="script-heading">Essential Oils</h2>
      <div class="oil-intro">
        <p>Our line of essential Oils are obtain by natural processes to keep the oils features...</p>
        <div class="oil-bottle" role="img" aria-label="Product photo of an essential oil bottle"></div>
      </div>
      <ul class="oil-list">
        <li>Clementine</li>
        <li>Lavadin Grosso</li>
        <li>Lemongrass</li>
        <li>Peppermint Premium</li>
        <li>Ylang Ylang</li>
        <li>Organic Ginger</li>
        <li>Organic Lavender</li>
        <li>Organic Lemon</li>
        <li>Organic Mandarin</li>
        <li>and many more...</li>
      </ul>
    </div>

    <div class="section-gap">
      <h2 class="script-heading">Our Memberships</h2>
      <div class="badge-row">
        <span class="badge" role="img" aria-label="Certified organic membership badge"></span>
        <span class="badge square" role="img" aria-label="Dunbrook crafted membership badge"></span>
        <span class="badge" role="img" aria-label="Organic industry membership badge"></span>
      </div>
    </div>
  </article>

  <article class="panel panel-skin">
    <h2 class="script-heading">Skin Care</h2>
    <p>Our Made with Organic Moisturising Cream is an exclusive range of premium products that have been specially formulated using certified organic ingredients.</p>
    <div class="product-grid">
      <div class="product"><div class="product-jar" role="img" aria-label="Product photo of moisturising cream jar"></div>Moisturising Cream <span class="price">$65</span></div>
      <div class="product"><div class="product-jar" role="img" aria-label="Product photo of eye cream jar"></div>Organic Eye Cream <span class="price">$95</span></div>
      <div class="product"><div class="product-jar" role="img" aria-label="Product photo of lip balm jar"></div>Organic Lip Balm <span class="price">$45</span></div>
      <div class="product"><div class="product-jar" role="img" aria-label="Product photo of aloe vera gel jar"></div>Organic Aloe Vera Gel <span class="price">$58</span></div>
    </div>
  </article>

  <article class="panel panel-body">
    <h2 class="script-heading">Body Care</h2>
    <p>Our Made with Organic Shower &amp; Bath Gel is an exclusive range of premium products that have been specially formulated using certified organic ingredients.</p>
    <div class="pair-products">
      <div class="product"><div class="pump-bottle" role="img" aria-label="Product photo of shower and bath gel pump bottle"></div>Shower and Bath Gel <span class="price">$65</span></div>
      <div class="product"><div class="pump-bottle lotion" role="img" aria-label="Product photo of body lotion pump bottle"></div>Certified Organic Body Lotion <span class="price">$75</span></div>
    </div>

    <div class="section-gap">
      <h2 class="script-heading">Hair Care</h2>
      <p>Our certified organic hair care range gently cleanses and nourishes hair using pure, naturally derived ingredients.</p>
      <div class="pair-products">
        <div class="product"><div class="pump-bottle shampoo" role="img" aria-label="Product photo of organic shampoo pump bottle"></div>Organic Shampoo <span class="price">$38</span></div>
        <div class="product"><div class="pump-bottle conditioner" role="img" aria-label="Product photo of organic conditioner pump bottle"></div>Organic Conditioner <span class="price">$38</span></div>
      </div>
    </div>
  </article>
</section>

<section class="cover">
  <div class="brand-block">
    <span class="brand-name">VEXMIRA</span>
  </div>
  <div class="mission">
    <p class="mission-title">Our Mission</p>
    <p>Vexmira’s mission is to make premium skin care products using only certified organic ingredients for a safer, purer world.</p>
  </div>
  <p class="tagline-script">An exhaustive resource of</p>
  <p class="tagline">spa and massage<br>treatments</p>
  <div class="cover-photo" role="img" aria-label="Photo of a woman receiving a mud face mask with candles and spa stones"></div>
  <div class="contact">
    <span class="contact-title">Contact Us</span>
    <span>www.vexmira.example</span>
  </div>
</section>

</body>
</html>
```